Vitamin Business Needs a Label Design

Hello. We are high-quality/healthy vitamin/supplement company, and we are in need of a Label design for a vitamin bottle.
Bottle will be either white or brown color. Label size will be 74mm*220mm. Please pick one logo from the attachments(you may use new design for the logo if you'd like to). On the front, please put two icon graphics(like certified organic sticker on food products) for "Kosher Certified" and "Vegetable Capsules". I attached sample of icon for your reference. I'm attaching files for the information. I will also put some example label designs on the brief page. Please let me know if you have any question. Thank you so much for the works!

Font styles to use
Serif
Sans Serif

Requirements
Must have
• Information on the files. I may put barcode later, so if possible, please leave a space for barcode. Thank you.
Nice to have
• White or Ivory color for the label background would be nice. But you may use different color if you'd like to. For your information, I prefer logo 2 over logo 1, but you can use any logo as long as the design looks great.
Should not have
• Please do not use sample icon or use icon from online. It is because there may be copyright issues. For color, please do not use dark colors for label background color. (if it looks very good, then its okay).

```html
<!DOCTYPE html>
<html lang="en">
<head>
<meta charset="utf-8">
<title>Verdavia Multivitamin Label</title>
<link href="https://fonts.googleapis.com/css2?family=Montserrat:wght@700;900&family=Open+Sans:wght@400;600;700&family=Oswald:wght@300;400;500&family=Raleway:wght@500;700&display=swap" rel="stylesheet">
<style>
:root{
  --paper:#ffffff;
  --mint:#e3efcf;
  --mint-deep:#cfe3b0;
  --leaf:#8cc63f;
  --leaf-soft:#a9d46a;
  --forest:#0f6b35;
  --forest-dark:#0b4f27;
  --slate:#5c5c5c;
  --ink:#222;
  --brown:#6b3f14;
}
*{margin:0;padding:0;box-sizing:border-box}
html,body{width:1200px;height:1200px;overflow:hidden;background:var(--paper)}
.canvas{position:relative;width:1200px;height:1200px}
.label{position:absolute;left:0;top:188px;width:1200px;height:404px;overflow:hidden;
  background:linear-gradient(180deg,var(--mint) 0%,#eef5e1 50%,var(--mint) 100%)}
.label-sweep{position:absolute;inset:0}
.top-tab{position:absolute;left:482px;top:0;width:262px;height:9px;background:var(--leaf);border-radius:0 0 10px 10px}

/* left info panel */
.info-panel{position:absolute;left:16px;top:18px;width:380px;height:372px;background:var(--paper);
  border:3px solid var(--forest);border-radius:18px;padding:12px 6px 6px 16px;
  font-family:'Oswald',sans-serif;font-weight:300;font-size:10.6px;line-height:13px;color:var(--ink)}
.info-panel p{margin:0}
.tag{background:var(--forest);color:#fff;border-radius:8px;padding:0 4px 0 3px;font-weight:400}
.info-panel b{font-weight:500}
.rule{height:2px;background:var(--forest);margin:8px 6px 8px -4px}
.gap{height:9px}
.store{font-family:'Open Sans',sans-serif;font-weight:700;font-size:12px;line-height:14px;text-align:center;margin-top:6px}

/* front panel */
.brand{position:absolute;left:453px;top:22px;width:317px;text-align:center;
  font-family:'Open Sans',sans-serif;font-weight:400;font-size:56px;color:var(--slate);letter-spacing:-1px}
.title{position:absolute;left:450px;width:322px;text-align:center;font-family:'Montserrat',sans-serif;font-weight:900;
  font-size:41px;line-height:36px;letter-spacing:-1px}
.title.vit{top:96px;color:var(--forest)}
.title.min{top:124px;color:var(--slate)}
.subtitle{position:absolute;left:560px;top:156px;width:210px;text-align:right;font-family:'Raleway',sans-serif;font-weight:700;font-size:24px;color:var(--brown)}
.support{position:absolute;left:496px;top:188px}
.support .lead{position:absolute;left:80px;top:18px;white-space:nowrap;font-family:'Raleway',sans-serif;font-weight:500;font-size:14px;color:var(--forest-dark)}
.support .item{position:absolute;white-space:nowrap;font-family:'Raleway',sans-serif;font-weight:700;font-size:22px;color:var(--forest-dark)}
.support .line{position:absolute;height:2px;background:var(--forest-dark)}
.count{position:absolute;left:634px;top:376px;font-family:'Open Sans',sans-serif;font-size:13px;color:var(--ink)}
.badge{position:absolute;border-radius:50%}
.badge.veg{left:434px;top:193px;width:96px;height:96px;background:var(--forest);border:6px solid #fff;box-shadow:0 0 0 2px var(--forest)}
.badge.kosher{left:428px;top:288px;width:72px;height:72px;background:#fff;border:5px solid var(--leaf)}
.dietary{position:absolute;left:436px;top:368px;font-family:'Open Sans',sans-serif;font-weight:700;font-size:9px;line-height:11px;color:var(--ink)}

/* facts panel */
.facts{position:absolute;left:824px;top:18px;width:290px;height:364px;background:#fff;border:2px solid var(--forest);border-radius:18px;
  padding:10px 14px 0 18px;font-family:'Oswald',sans-serif;font-weight:300;font-size:7.4px;color:var(--ink)}
.facts h2{font-family:'Open Sans',sans-serif;font-weight:700;font-size:13px}
.facts .serving{font-family:'Open Sans',sans-serif;font-size:7.5px}
.facts .head{display:flex;justify-content:space-between;font-family:'Open Sans',sans-serif;font-weight:700;font-size:7px;border-bottom:2px solid var(--ink);padding-bottom:1px;margin-bottom:3px}
.facts table{width:100%;border-collapse:collapse}
.facts td{height:11.65px;line-height:9px;white-space:nowrap}
.facts td.amt{width:46px}
.facts td.dv{text-align:right;width:70px}
.facts .foot{text-align:right;font-size:7.2px;margin-top:8px}
.facts .disc{font-family:'Open Sans',sans-serif;font-weight:700;font-size:6.3px;line-height:8.5px;margin-top:4px}

.barcode-space{position:absolute;left:1124px;top:28px;width:66px;height:144px;background:#fff;border:2px solid var(--ink)}
.distributor{position:absolute;left:1130px;top:332px;transform-origin:0 0;transform:rotate(-90deg);
  font-family:'Open Sans',sans-serif;font-weight:700;font-size:11px;line-height:16px;color:var(--slate);white-space:nowrap}
.distributor .web{color:var(--forest)}
</style>
</head>
<body>
<div class="canvas">
  <section class="label">
    <svg class="label-sweep" width="1200" height="404" role="img" aria-label="Soft green swoosh background">
      <path d="M0 0 C200 40 300 120 420 150 L420 210 C280 180 120 120 0 90 Z" fill="var(--mint-deep)" opacity=".6"/>
      <path d="M760 300 C900 260 1050 250 1200 240 L1200 404 L760 404 Z" fill="var(--mint-deep)" opacity=".5"/>
      <path d="M765 252 L820 246" stroke="var(--forest)" stroke-width="3"/>
      <circle cx="642" cy="330" r="142" fill="var(--leaf-soft)" opacity=".55"/>
      <circle cx="648" cy="338" r="132" fill="var(--leaf)"/>
    </svg>
    <div class="top-tab"></div>

    <div class="info-panel">
      <p><span class="tag">What is a Kosher Product?</span> Kosher certified product is a food or product that complies with Kosher food laws, which include strict policies on maintaining its quality, cleanliness, and pureness.</p>
      <p><span class="tag">What is a Vegetable Capsule?</span> Vegetable capsule is a form of pharmaceutical dosage made with natural vegetable cellulose which does not contain preservatives, chemical additives, gelatin, wheat, and animal-derived ingredients. It is easy to swallow and dissolves quickly in the stomach for absorption.</p>
      <p><span class="tag">Benefits of Verdavia Multivitamin Supplement</span> Overall Health - It helps you to maintain overall healthiness by supplying essential nutrients you may not get enough during the day.</p>
      <p><b>Immune System</b> - Antioxidants such as Vitamins A, C, E, and Selenium helps improve immune function.</p>
      <p><b>Energy - B</b>- Vitamins support daily energy needs by helping body to convert food into energy.</p>
      <p><b>Metabolism</b> - Minerals including Zinc, Iron, Selenium, and B-Vitamins help support metabolism.</p>
      <div class="rule"></div>
      <p><b>SUGGESTED USE:</b> Adults: Take one (1) tablet daily, preferably with a meal. Do not exceed suggested use. If you are pregnant, nursing, or taking medication, consult your doctor before use.</p>
      <div class="gap"></div>
      <p><b>WARNING:</b> Accidental overdose of iron-containing products is a leading cause of fatal poisoning in children under 6. Keep this product out of reach of children. In case of accidental overdose, call a doctor or poison control center immediately.</p>
      <p class="store">Store at cool, dry place. Keep bottle firmly closed.<br>Do not use if seal is missing, torn, or damaged.</p>
    </div>

    <div class="brand">Verdavia</div>
    <div class="title vit">MULTIVITAMIM</div>
    <div class="title min">MULTIMINERAL</div>
    <div class="subtitle">Supplement</div>

    <div class="support">
      <span class="lead">Essential support for:</span>
      <span class="item" style="left:67px;top:38px">Overall Health</span>
      <span class="line" style="left:76px;top:70px;width:196px"></span>
      <span class="item" style="left:47px;top:71px">Immune System</span>
      <span class="line" style="left:46px;top:103px;width:226px"></span>
      <span class="item" style="left:150px;top:104px">Energy</span>
      <span class="line" style="left:46px;top:136px;width:226px"></span>
      <span class="item" style="left:96px;top:136px">Metabolism</span>
    </div>
    <div class="count">180 CAPSULES</div>

    <div class="badge veg"></div>
    <div class="badge kosher"></div>
    <div class="dietary">Dietary<br>Supplement</div>

    <div class="facts">
      <h2>Supplement Facts</h2>
      <div class="serving">Serving Size 1 Capsule</div>
      <div class="head"><span>Amount Per Serving</span><span>% DV</span></div>
      <table>
        <tr><td>Vitamin A (beta-carotene)</td><td class="amt">2000 IU</td><td class="dv">(1200mcg) 40%</td></tr>
        <tr><td>vitamin C (ascorbic acid) 1</td><td class="amt">50mg</td><td class="dv">250%</td></tr>
        <tr><td>vitamin D (cholecalciferol)</td><td class="amt">400 IU</td><td class="dv">100%</td></tr>
        <tr><td>vitamin E (DL-alpha tocopherol acetate 50%)</td><td class="amt">30 IU</td><td class="dv">100%</td></tr>
        <tr><td>vitamin B1 (thiamine HCl)</td><td class="amt">7</td><td class="dv">450%</td></tr>
        <tr><td>vitamin B2 (riboflavin)</td><td class="amt">7.5</td><td class="dv">440%</td></tr>
        <tr><td>vitamin B3 (Niacinamide)</td><td class="amt">20mg</td><td class="dv">100%</td></tr>
        <tr><td>vitamin B6 (pyridoxine HCl)</td><td class="amt">7.5mg</td><td class="dv">375%</td></tr>
        <tr><td>Folic acid</td><td class="amt">400mcg</td><td class="dv">100%</td></tr>
        <tr><td>vitamin B12 (cyanocobalamin)</td><td class="amt">27mcg</td><td class="dv">225%</td></tr>
        <tr><td>Biotin</td><td class="amt">300mcg</td><td class="dv">100%</td></tr>
        <tr><td>Vitamin B5 (D-Calcium pantothenate)</td><td class="amt">10mg</td><td class="dv">100%</td></tr>
        <tr><td>Calcium (citrate 21%)</td><td class="amt">25mg</td><td class="dv">5%</td></tr>
        <tr><td>Iron (ferrous fumarate)</td><td class="amt">6mg</td><td class="dv">33%</td></tr>
        <tr><td>Iodine (from Kelp)</td><td class="amt">150mcg</td><td class="dv">100%</td></tr>
        <tr><td>Magnesium (citrate 16%)</td><td class="amt">50mg</td><td class="dv">6%</td></tr>
        <tr><td>Zinc Citrate 31%</td><td class="amt">15mg</td><td class="dv">100%</td></tr>
        <tr><td>Selenium (AAC 2%)</td><td class="amt">30mcg</td><td class="dv">42%</td></tr>
        <tr><td>Copper Glycinate or Aspartate 10%</td><td class="amt">2mg</td><td class="dv">100%</td></tr>
        <tr><td>Manganese (chelate 20%)</td><td class="amt">2mg</td><td class="dv">100%</td></tr>
        <tr><td>Chromium (picolinate 15%)</td><td class="amt">120mcg</td><td class="dv">100%</td></tr>
        <tr><td>Molybdenum Glycinate Chelate 2.5%</td><td class="amt">75mcg 1</td><td class="dv">00%</td></tr>
        <tr><td>Boron (rice protein complex)</td><td class="amt">150mcg</td><td class="dv">*</td></tr>
      </table>
      <div class="foot">* % Daily Value (DV) not established</div>
      <div class="disc">[*This statement has not been evaluated by the Food and Drug Administration. This product is not intended to diagnose, treat, cure, or prevent any disease.]</div>
    </div>

    <div class="barcode-space"></div>
    <div class="distributor">Distributed by: Greenroot LLC<br>Cedar Vale, CA 90014<br><span class="web">Verdavia.com | Made in USA</span></div>
  </section>
</div>
</body>
</html>
```